Talverno Industrial Services Decontamination

We need a Brochure Design for a new company based in Jubail Eastern Region in Saudi Arabia. The name of our new Company is "Talverno Industrial Services Company", Our Industrial Services include liquid/dry vacuuming, hydro jetting and blasting, boiler cleaning, condenser and heat exchanger tube cleaning, Tank Cleaning, Decontamination, chemical cleaning, and pipe cleaning and removal etc.

We are dedicated to providing excellent service and fast turn around for completing projects on-time, within budget, and without incident.
Updates

I have uploaded the Logo, I am also putting a 40 US$ Participation Payment

Project Deadline Extended
Reason: Required more designs

Target Market(s)

Petrochemical Plants, Oil & Gas Companies, EPC Contractors etc.

Industry/Entity Type

It Company

Requirements
Must have
• Rich with high resolution pictures and Graphics. Designer has to provide these pictures and graphics. If there is extra charges for the pictures we will pay.

Good pictures for each project. Brochure should be very Informative and not boring. Should have highlight text, bubbled text etc.

The maximum pages should be from 4-6.

```html
<!DOCTYPE html>
<html lang="en">
<head>
<meta charset="utf-8">
<title>Talverno Industrial Services Decontamination</title>
<link href="https://fonts.googleapis.com/css2?family=Source+Sans+3:wght@400;600;700&display=swap" rel="stylesheet">
<style>
  :root {
    --paper: #ffffff;
    --slate: #8f8f8f;
    --yellow: #f4d631;
    --title-yellow: #f5d327;
    --pill: #ebebeb;
    --pill-text: #4a4a4a;
    --label-grey: #8a8a8a;
    --photo-dark: #4b4a47;
    --photo-light: #a9a49a;
    --white: #ffffff;
  }
  * { margin: 0; padding: 0; box-sizing: border-box; }
  html, body { width: 1200px; height: 558px; overflow: hidden; background: var(--paper); }
  body { font-family: "Source Sans 3", "Myriad Pro", Arial, sans-serif; position: relative; }

  .spread { position: absolute; left: 72px; top: 70px; width: 1056px; height: 407px; }
  .page { position: absolute; top: 0; height: 407px; width: 528px; overflow: hidden; }
  .page--intro { left: 0; background: var(--slate); color: var(--white); }
  .page--benefits { left: 528px; background: var(--yellow); }

  .folio { position: absolute; top: 19px; font-size: 7.5px; color: var(--title-yellow); white-space: nowrap; }
  .page--intro .folio { left: 38px; }
  .page--benefits .folio { right: 40px; color: #ddd6b4; }

  .section-title { position: absolute; left: 37px; top: 79px; font-size: 16px; font-weight: 400; color: var(--title-yellow); line-height: 1; }

  .intro-copy { position: absolute; left: 38px; top: 103px; width: 243px; font-size: 5.9px; line-height: 7.4px; }
  .intro-copy p { margin-bottom: 4.2px; }

  .impact-list { position: absolute; left: 308px; top: 106px; width: 190px; font-size: 5.6px; }
  .impact-list h3 { font-size: 5.8px; font-weight: 700; margin-bottom: 3px; }
  .impact-list ul { list-style: none; margin-bottom: 11px; }
  .impact-list li { position: relative; padding-left: 9px; line-height: 10.4px; white-space: nowrap; }
  .impact-list li::before { content: ""; position: absolute; left: 0; top: 2.7px; width: 5px; height: 5px; background: var(--title-yellow); }

  .site-photo { position: absolute; left: 0; top: 0; }

  .column { position: absolute; top: 97px; width: 120px; }
  .column--benefits { left: 34px; }
  .column--applications { left: 168px; }
  .column h3 { text-align: center; font-size: 6px; font-weight: 600; color: var(--label-grey); height: 9.8px; line-height: 6px; }
  .column ul { list-style: none; }
  .column li {
    height: 18.4px; margin-bottom: 4.8px; border-radius: 6px; background: var(--pill);
    color: var(--pill-text); font-size: 6.4px; display: flex; align-items: center; justify-content: center;
    white-space: nowrap; box-shadow: 0 0.5px 1px rgba(0,0,0,0.12);
  }
</style>
</head>
<body>
<div class="spread">
  <section class="page page--intro">
    <div class="folio">03 | Talverno Industrial Services Co.</div>
    <h1 class="section-title">Decontamination</h1>
    <div class="intro-copy">
      <p>Talverno have Corvane - Swift Entry, developed proven alternative to the 'steaming' of refinery process units that saves time, maximizes efficiency and offers operators complete peace of mind.</p>
      <p>A proven alternative Chemical decontamination of refinery process units reduces the preparation time for entry compared to traditional steaming out and hydrocarbon flushing.</p>
      <p>The chemical washing procedure rapidly penetrates deposits and suspends them for flushing out of the system, providing cleaner internal conditions. At the same time, residual hydrocarbons are captured and held in a temporary emulsion and transported away. Steaming alone cannot do this.</p>
      <p>Saving you time and money During major turnarounds, safe entry conditions for inspection and maintenance personnel are critical to the overall time-line.</p>
      <p>Chemical decontamination can provide clean, gas-free conditions, with no pyrophorics issues, that enable internal work, including 'hot work', to proceed rapidly. Compared to steaming-out a timesaving of 1 – 2 days can be achieved on large vessels, which in turn produces significant cost savings for the refinery.</p>
      <p>Health and safety benefits Health and safety improvements are considerable as personnel exposure to Hydrogen Sulphide and hazardous L.E.L. conditions is eliminated. Pyrophoric deposits are neutralized and the potential for spontaneous fires removed, leaving cleaner internals which means safer working conditions for crews.</p>
      <p>The decontamination process uses proven chemical technology that meets all current refinery regulations for vessel preparation, and is also biodegradable, minimizing overall Environmental impact.</p>
      <p>Talverno- Corvane Decontamination Chemicals minimize risk during maintenance operations.</p>
    </div>
    <div class="impact-list">
      <h3>Safety Health Environment Impact :</h3>
      <ul>
        <li>Pyrophoric compounds deactivation (FeS)</li>
        <li>Process equipment decontamination</li>
        <li>Minimized Air emission</li>
        <li>Hydrocarbons absorption from process fouling</li>
        <li>Provide oil-free surfaces</li>
        <li>Cleaning water has no impact on WWT</li>
        <li>Cleaning Water has low BOD-COD-TOC</li>
        <li>Closed-loop circulation</li>
      </ul>
      <h3>Cost Impact :</h3>
      <ul>
        <li>TCO optimization</li>
        <li>Reduced Turnaround time</li>
        <li>Less manpower demand</li>
        <li>Reduced disposal costs</li>
        <li>Restore equipment efficiency / capacity</li>
      </ul>
      <h3>Environmental sustainability through:</h3>
      <ul>
        <li>Water savings</li>
        <li>Minimization of waste generation and disposal</li>
        <li>No pollution to atmosphere and environment</li>
      </ul>
    </div>
  </section>

  <section class="page page--benefits">
    <svg class="site-photo" width="528" height="407" viewBox="0 0 528 407">
      <defs>
        <linearGradient id="photoTone" x1="0" y1="0" x2="1" y2="1">
          <stop offset="0" stop-color="#9a958c"/>
          <stop offset="0.5" stop-color="#6f6a63"/>
          <stop offset="1" stop-color="var(--photo-dark)"/>
        </linearGradient>
      </defs>
      <polygon role="img" aria-label="Photo of an industrial safety shower station outside a glass-fronted plant building"
               points="372,0 528,0 528,407 284,407 218,342 218,138" fill="url(#photoTone)"/>
      <polygon points="400,0 434,0 410,258 528,294 528,322 356,282" fill="var(--yellow)"/>
      <polygon points="448,100 528,86 528,112 470,122" fill="var(--yellow)"/>
    </svg>
    <div class="folio">Talverno Industrial Services Co. | 04</div>

    <div class="column column--benefits">
      <h3>Major Benifits</h3>
      <ul>
        <li>Zero LEL</li>
        <li>Zero H₂S</li>
        <li>Less than 0.5 ppm Benzene</li>
        <li>Gas Free conditions</li>
        <li>No pyrophoric Issues</li>
        <li>No Steaming out or N₂ purging required</li>
        <li>Partial Scales Removal</li>
        <li>Time saving</li>
        <li>Reduced Cost</li>
        <li>Health &amp; safety</li>
        <li>Bio Degradable chemicals</li>
        <li>Works on ambient temperature</li>
      </ul>
    </div>
    <div class="column column--applications">
      <h3>Applications</h3>
      <ul>
        <li>Crude Units - Vacuum Units</li>
        <li>Fluid Catalytic Crackers</li>
        <li>HDS Units</li>
        <li>Distillate Processing Units</li>
        <li>Amine Units</li>
        <li>Desalters</li>
        <li>Flare Systems</li>
        <li>Visbreakers</li>
        <li>Heat Exchangers</li>
        <li>Pipelines</li>
      </ul>
    </div>
  </section>
</div>
</body>
</html>
```